Car wrap desgin Talvin

We’d like new design proposals for passenger cars (KM Dorvane & Brčka Ulvaro eX). Both vehicles are white. I don’t want the entire car to be wrapped in yellow. more informations about us, you will find under: https://www.talviiiin.ch/home

Less is more. Keep it simple, clean, and stylish - and only with yellow ond black as color beside the with car

```html
<!DOCTYPE html>
<html lang="de">
<head>
<meta charset="utf-8">
<title>Talvin – Fahrzeugbeschriftung</title>
<link href="https://fonts.googleapis.com/css2?family=Oswald:wght@500;600&family=Archivo:wght@400&display=swap" rel="stylesheet">
<style>
  :root {
    --bg: #e3e4e5;
    --body-white: #f6f6f6;
    --body-edge: #cfd1d3;
    --glass: #3b3f43;
    --tyre: #2a2c2e;
    --brand-yellow: #dcc81c;
    --brand-black: #1e1e1e;
  }
  html, body {
    margin: 0;
    padding: 0;
    width: 1200px;
    height: 1200px;
    overflow: hidden;
    background: var(--bg);
  }
  .wrap-layout {
    display: block;
    width: 1200px;
    height: 1200px;
  }
  .vehicle-body { fill: var(--body-white); stroke: var(--body-edge); stroke-width: 2; }
  .vehicle-glass { fill: var(--glass); }
  .vehicle-seam { stroke: var(--body-edge); stroke-width: 2; fill: none; }
  .vehicle-wheel { fill: var(--tyre); }
  .accent-yellow { fill: var(--brand-yellow); }
  .accent-black { fill: var(--brand-black); }
  .brand-name {
    font-family: "Oswald", sans-serif;
    font-weight: 600;
    font-size: 36px;
    letter-spacing: 9px;
    fill: var(--brand-black);
  }
  .brand-tagline {
    font-family: "Archivo", sans-serif;
    font-weight: 400;
    font-size: 12.5px;
    letter-spacing: 1.4px;
    fill: var(--brand-black);
  }
  .contact-line {
    font-family: "Oswald", sans-serif;
    font-weight: 500;
    font-size: 21px;
    letter-spacing: 0.6px;
    fill: var(--brand-black);
  }
</style>
</head>
<body>
<svg class="wrap-layout" viewBox="0 0 1200 1200" xmlns="http://www.w3.org/2000/svg">
  <defs>
    <clipPath id="body-clip">
      <path d="M62,825 L60,700 Q65,675 90,670 L312,619 L500,525 Q700,505 950,506 L1112,587 Q1130,600 1140,650 L1156,750 L1150,825 L1050,838 A105,105 0 0 0 832,838 L346,838 A105,105 0 0 0 136,838 Z"/>
    </clipPath>
  </defs>

  <g class="vehicle">
    <path class="vehicle-body" d="M62,825 L60,700 Q65,675 90,670 L312,619 L500,525 Q700,505 950,506 L1112,587 Q1130,600 1140,650 L1156,750 L1150,825 L1050,838 A105,105 0 0 0 832,838 L346,838 A105,105 0 0 0 136,838 Z"/>
    <path class="vehicle-glass" d="M330,625 L505,535 Q700,520 930,520 L1010,592 Z"/>
  </g>

  <g class="wrap-graphics" clip-path="url(#body-clip)">
    <polygon class="accent-yellow front-band" points="60,705 366,665 366,759 60,759"/>
    <rect class="accent-yellow door-panel" x="366" y="665" width="284" height="94"/>
    <rect class="accent-black rocker-line" x="366" y="790" width="700" height="6"/>
    <rect class="accent-yellow rear-square" x="1040" y="672" width="44" height="44"/>
  </g>

  <g class="vehicle-details">
    <line class="vehicle-seam" x1="650" y1="625" x2="650" y2="838"/>
    <line class="vehicle-seam" x1="366" y1="628" x2="366" y2="838"/>
    <circle class="vehicle-wheel" cx="241" cy="830" r="92" role="img" aria-label="Vorderrad"/>
    <circle class="vehicle-wheel" cx="941" cy="830" r="92" role="img" aria-label="Hinterrad"/>
  </g>

  <g class="brand-block">
    <text class="brand-name" x="390" y="722">TALVIIIIN</text>
    <text class="brand-tagline" x="390" y="747">HAUSTECHNIK + BAUSPENGLEREI</text>
  </g>

  <g class="contact-block">
    <text class="contact-line" x="675" y="708">+41 41 387 62 00</text>
    <text class="contact-line" x="675" y="736">INFOTALVIIIIN.CH</text>
  </g>
</svg>
</body>
</html>
```